Penwick Halloway Stage Foundation Poster Design for "Dorsey and Kettleby Celebrate Songs of the Sc...

We need a design for an 11" wide by 17" high (vertical) poster advertising an organ concert. Design should have a 1/8" extra for bleed all around.
Here are the particulars:
Dorsey and Kettleby Salute Songs of the Screen
A Duo Concert on Theatre Organ
and Grand Piano
Sunday, November 16, 2025 at 2:30 p.m.
Penwick Halloway Auditorium,
2716 North 8th Court (Penwick Halloway Blvd), Tulsa, OK 74129
All seats reserved. All tickets sold on-line beginning Sept. 15, 2025, 12:01 a.m. www.PenwickHallowayStage.com
Alden Dorsey returns to the historic Penwick Halloway Auditorium on the Brellin Theatre Organ, along with Artist-in-Residence Gus Kettleby to Salute Songs of the Screen! They will perform movie songs on the theatre organ and also play duets with the 1939 Corvath Grand Piano. Alden Dorsey is one of America’s busiest theatre organists, performing over 30 concerts and silent film presentations each year across the US and abroad. In 2012, he was named the National Cinema Console Guild’s Console Player of the Season and was the youngest person ever to receive the prestigious honor. Gus Kettleby was a singer/pianist on the NYC Hotel Circuit, a theatre pit pianist, and a touring keyboardist and musical director for 12 years with the Pellam prize-winning shows Owls, Lemon Darlings, Riverjoy and Tiny Barn of Shivers in 150+ cities nationally and abroad.
To get a better feel for our organization, go to the website landing page for Pinwheel, our next show: www.PenwickHallowayStage.com
Then, click on MENU
Click on About Us

```html
<!DOCTYPE html>
<html lang="en">
<head>
<meta charset="utf-8">
<title>Dorsey and Kettleby – Concert Poster</title>
<link rel="stylesheet" href="https://fonts.googleapis.com/css2?family=Cinzel:wght@600;700&family=Roboto:wght@400;500&display=swap">
<style>
  :root{
    --page:#e9e9eb;
    --blue-deep:#1a0f9c;
    --blue:#2a22c4;
    --blue-dark:#0c0670;
    --gold:#f3cf5a;
    --gold-light:#fff2c4;
    --red:#d70f1c;
    --red-dark:#9e0712;
    --white:#ffffff;
  }
  *{margin:0;padding:0;box-sizing:border-box}
  html,body{width:1200px;height:2547px;overflow:hidden;background:var(--page)}
  .poster{
    position:absolute;left:50px;top:424px;
    width:787px;height:1215px;
    transform:scale(1.3977);transform-origin:0 0;
    background:
      radial-gradient(ellipse at 85% 10%, var(--blue-dark) 0%, transparent 45%),
      linear-gradient(180deg,var(--blue) 0%,var(--blue-deep) 60%,var(--blue) 100%);
    overflow:hidden;
    font-family:'Roboto',sans-serif;color:var(--white);
  }
  .title{
    position:absolute;left:0;width:100%;text-align:center;
    font-family:'Cinzel',serif;font-weight:700;
    background:linear-gradient(180deg,var(--gold) 20%,var(--gold-light) 100%);
    -webkit-background-clip:text;background-clip:text;color:transparent;
    line-height:1;white-space:nowrap;
  }
  .title-names{top:28px;font-size:82px;letter-spacing:1px}
  .title-names span{display:block;margin-bottom:-2px}
  .title-instrument{top:264px;font-size:66px}
  .ribbon{position:absolute;left:0;top:180px;width:787px;height:90px}
  .performer-photo{
    position:absolute;left:0;top:335px;width:787px;height:550px;
    background:
      radial-gradient(ellipse at 30% 45%, #2b2a3a 0%, transparent 40%),
      radial-gradient(ellipse at 80% 50%, #6b3518 0%, transparent 45%),
      linear-gradient(180deg,transparent 0%,#8a6a3a 35%,#5a3b50 70%,transparent 100%);
  }
  .date-box{
    position:absolute;left:108px;top:889px;width:569px;height:70px;
    border:3px solid var(--gold);
    display:flex;align-items:center;justify-content:center;
    font-family:'Cinzel',serif;font-weight:600;font-size:25px;color:var(--gold);
    white-space:nowrap;
  }
  .details{position:absolute;left:0;width:100%;text-align:center;white-space:nowrap}
  .venue{top:978px;font-size:27px}
  .address{top:1022px;font-size:17.5px}
  .tickets{top:1048px;font-size:16.5px}
  .seats{top:1072px;font-size:22px}
  .website{top:1158px;font-size:18px}
</style>
</head>
<body>
<main class="poster">
  <h1 class="title title-names"><span>Dorsey and</span><span>Kettleby</span></h1>

  <svg class="ribbon" viewBox="0 0 787 90" aria-hidden="true">
    <polygon points="62,28 150,28 150,80 86,80 108,54" fill="var(--red-dark)"/>
    <polygon points="725,28 637,28 637,80 701,80 679,54" fill="var(--red-dark)"/>
    <path d="M138,20 Q393,-2 650,20 L640,72 Q393,50 148,72 Z" fill="var(--red)"/>
    <path id="ribbon-line" d="M160,58 Q393,30 630,58" fill="none"/>
    <text font-family="Roboto, sans-serif" font-size="15.5" fill="var(--white)" text-anchor="middle">
      <textPath href="#ribbon-line" startOffset="50%">Salute Songs of the ScreenA Duo Concert on Theatre Organ and</textPath>
    </text>
  </svg>

  <h2 class="title title-instrument">Grand Piano</h2>

  <div class="performer-photo" role="img" aria-label="Photo of a smiling organist in a dark suit seated at a theatre organ console"></div>

  <div class="date-box">Sunday, November 16, 2025 at 2:30 p.m.</div>

  <p class="details venue">Penwick Halloway Auditorium</p>
  <p class="details address">2716 North 8th Court (Penwick Halloway Blvd), Tulsa, OK 74129</p>
  <p class="details tickets">All tickets sold on-line beginning Sept. 15, 2025, 12:01 a.m.</p>
  <p class="details seats">All seats reserved</p>
  <p class="details website">www.PenwickHallowayStage.com</p>
</main>
</body>
</html>
```